Flyer for a marketing

We are a holistic mental health facility in need of a flyer to help promote our services and encourage more people to seek care. See the attachment to tell you more. We prefer warm green colors or rich blue. Thank you.

```html
<!DOCTYPE html>
<html lang="en">
<head>
<meta charset="utf-8">
<title>Evergreen Mind Health and Wellness – Flyer</title>
<link rel="stylesheet" href="https://fonts.googleapis.com/css2?family=Libre+Baskerville:wght@400;700&family=Noto+Serif:wght@400;500&family=Open+Sans:wght@400;600;700&display=swap">
<style>
  :root {
    --leaf-green: #6cbf4a;
    --box-green: #3db54a;
    --box-blue: #0f6c9c;
    --sky: #c6e4ef;
    --pink: #e0116f;
    --navy: #2a3f8f;
    --ink: #1f2a3a;
    --white: #ffffff;
    --strip: #e8e8e8;
    --serif: "Libre Baskerville", Georgia, serif;
    --head: "Noto Serif", Georgia, serif;
    --sans: "Open Sans", Arial, sans-serif;
  }
  * { box-sizing: border-box; margin: 0; padding: 0; }
  html, body { width: 856px; height: 1200px; overflow: hidden; background: var(--sky); }
  .flyer { position: relative; width: 856px; height: 1200px; overflow: hidden; background: var(--sky); font-family: var(--sans); }
  .backdrop { position: absolute; inset: 0; }

  .brand { position: absolute; left: 50px; top: 40px; width: 340px; height: 170px; }
  .brand-mark { position: absolute; left: 20px; top: 40px; width: 110px; height: 110px; border-radius: 50%; background: var(--white); }
  .brand-rule { position: absolute; left: 168px; top: 0; width: 2px; height: 170px; background: var(--white); }
  .brand-name { position: absolute; left: 200px; top: 10px; font-family: var(--serif); font-weight: 700; font-size: 22px; line-height: 28px; color: var(--white); }
  .brand-tag { position: absolute; left: 76px; top: 200px; font-size: 16.5px; color: var(--white); }
  .slogan { position: absolute; left: 84px; top: 236px; font-family: var(--serif); font-size: 22px; color: var(--ink); }

  .headline { position: absolute; left: 60px; top: 430px; width: 780px; font-family: var(--head); text-shadow: 1px 1px 1px rgba(0,0,0,.25); }
  .headline .l1 { display: block; margin-left: 26px; font-size: 48px; line-height: 56px; color: var(--pink); }
  .headline .l2 { display: block; font-size: 35px; line-height: 42px; color: var(--pink); }
  .headline .l3 { display: block; margin-left: 24px; font-size: 21px; line-height: 40px; color: var(--navy); }
  .navy { color: var(--navy); }
  .pink-big { color: var(--pink); font-size: 32px; }

  .features { position: absolute; left: 40px; top: 616px; width: 362px; list-style: none; }
  .feature { display: flex; align-items: center; height: 82px; margin-bottom: 14.5px; color: var(--white); }
  .feature.green { background: var(--box-green); }
  .feature.blue { background: var(--box-blue); }
  .feature-icon { width: 64px; height: 100%; display: flex; align-items: center; justify-content: center; border-right: 1px solid rgba(255,255,255,.6); }
  .feature-text { padding-left: 20px; font-weight: 600; font-size: 16.5px; line-height: 23px; }

  .callout { position: absolute; left: 424px; top: 616px; width: 387px; height: 179px; background: var(--pink); padding: 10px 8px 0 8px; }
  .callout-head { background: var(--white); height: 72px; font-family: var(--serif); font-weight: 700; font-variant: small-caps; color: var(--pink); font-size: 19px; line-height: 27px; text-align: center; padding-top: 8px; letter-spacing: .3px; }
  .callout-body { color: var(--white); font-weight: 700; font-size: 16.5px; line-height: 25px; padding: 12px 14px 0 16px; text-align: justify; }

  .contact { position: absolute; left: 428px; top: 868px; color: var(--ink); font-weight: 600; font-size: 16.5px; line-height: 24px; }
  .contact .lines { display: grid; grid-template-columns: 64px auto; margin-top: 12px; }
  .contact .web { margin-top: 12px; }
  .contact .web div { display: flex; align-items: center; gap: 8px; }

  .partners { position: absolute; left: 0; top: 1097px; width: 856px; height: 103px; background: var(--strip); display: flex; align-items: center; justify-content: space-around; padding: 0 40px; }
  .badge { height: 38px; border-radius: 4px; }
</style>
</head>
<body>
<main class="flyer">
  <svg class="backdrop" width="856" height="1200" viewBox="0 0 856 1200" aria-hidden="true">
    <path d="M0,0 H430 V300 L400,296 L380,304 L352,298 L330,306 L300,300 L276,310 L250,304 L226,312 C150,330 60,370 0,420 Z" fill="var(--leaf-green)"/>
    <path d="M226,312 L250,304 L276,310 L300,300 L330,306 L352,298 L380,304 L400,296 L430,300 L430,308 L400,304 L380,312 L352,306 L330,314 L300,308 L276,318 L250,312 L226,320 Z" fill="var(--white)" opacity=".85"/>
    <path d="M540,472 C660,468 780,425 856,360 V440 C780,472 700,478 600,478 Z" fill="var(--pink)"/>
  </svg>
  <svg class="backdrop" width="856" height="1200" viewBox="0 0 856 1200" role="img" aria-label="Photo of a grandmother pouring a warm drink for a young girl in an autumn forest">
    <defs>
      <linearGradient id="forest" x1="0" y1="0" x2="1" y2="1">
        <stop offset="0" stop-color="#c9a56a"/>
        <stop offset=".5" stop-color="#8a8f6a"/>
        <stop offset="1" stop-color="#4f5f6f"/>
      </linearGradient>
    </defs>
    <path d="M395,0 H856 V360 C780,425 660,468 560,470 C450,470 370,360 375,220 C378,120 390,50 395,0 Z" fill="url(#forest)"/>
  </svg>

  <header class="brand">
    <span class="brand-mark"></span>
    <span class="brand-rule"></span>
    <p class="brand-name">Evergreen<br>Mind<br>Health<br>and<br>Wellness</p>
  </header>
  <p class="brand-tag">A Professional Nursing Corporation</p>
  <p class="slogan">The Care You Deserve</p>

  <h1 class="headline">
    <span class="l1">Evergreen</span>
    <span class="l2"><span class="navy">Mind</span> Health and Wellness,</span>
    <span class="l3">where deserving patients meet <span class="pink-big">compassionate</span> providers</span>
  </h1>

  <ul class="features">
    <li class="feature green">
      <span class="feature-icon"><svg width="40" height="40" viewBox="0 0 40 40" fill="none" stroke="#fff" stroke-width="1.6"><path d="M14 32v-6c-4-2-6-6-6-10a12 12 0 0 1 24 0l3 6h-3v6h-6v4"/><rect x="16" y="11" width="8" height="8"/></svg></span>
      <span class="feature-text">We are an integrative holistic psychiatric center.</span>
    </li>
    <li class="feature blue">
      <span class="feature-icon"><svg width="40" height="40" viewBox="0 0 40 40" fill="none" stroke="#fff" stroke-width="1.6"><path d="M14 34v-6c-4-2-6-6-6-10a12 12 0 0 1 24 0l3 6h-3v6h-6v4"/><path d="M20 16c-4-2-4-7 0-9 4 2 4 7 0 9z"/></svg></span>
      <span class="feature-text">Our mission is to provide compassionate quality care</span>
    </li>
    <li class="feature green">
      <span class="feature-icon"><svg width="40" height="40" viewBox="0 0 40 40" fill="none" stroke="#fff" stroke-width="1.6"><path d="M14 34v-6c-4-2-6-6-6-10a12 12 0 0 1 24 0l3 6h-3v6h-6v4"/><circle cx="20" cy="17" r="4"/><circle cx="20" cy="17" r="7" stroke-dasharray="3 2"/></svg></span>
      <span class="feature-text">We provide psychiatric services including medication management &amp; psychotherapy</span>
    </li>
    <li class="feature blue">
      <span class="feature-icon"><svg width="44" height="40" viewBox="0 0 44 40" fill="none" stroke="#fff" stroke-width="1.6"><circle cx="10" cy="18" r="4"/><circle cx="34" cy="18" r="4"/><path d="M4 34c0-6 3-9 6-9s6 3 6 9M28 34c0-6 3-9 6-9s6 3 6 9"/><rect x="14" y="4" width="16" height="8" rx="3"/></svg></span>
      <span class="feature-text">We listen, care, and empower you to live better.</span>
    </li>
    <li class="feature green">
      <span class="feature-icon"><svg width="40" height="40" viewBox="0 0 40 40" fill="none" stroke="#fff" stroke-width="1.6"><rect x="9" y="7" width="22" height="28" rx="2"/><rect x="15" y="4" width="10" height="5"/><path d="M14 20h6M17 17v6M14 28h12"/></svg></span>
      <span class="feature-text">We accept major insurances.</span>
    </li>
  </ul>

  <section class="callout">
    <p class="callout-head">We are accepting new patients,<br>no waiting list.</p>
    <p class="callout-body">Your mental health matters, so make it a priority and call us today for an appointment.</p>
  </section>

  <address class="contact" style="font-style: normal;">
    <div>Evergreen Mind Health and Wellness, APNC<br>1850 Alder Creek Road, Suite 300<br>Fernhill, CA 93999.</div>
    <div class="lines"><span>Phone</span><span>: (555) 214-7730</span><span>Fax</span><span>: (555) 214-7731</span></div>
    <div class="web">
      <div><svg width="14" height="10" viewBox="0 0 14 10"><rect width="14" height="10" fill="var(--box-blue)"/><path d="M0 0l7 5 7-5" stroke="#fff" fill="none"/></svg>info@evergreenmindhealth.com</div>
      <div><svg width="14" height="14" viewBox="0 0 14 14" fill="none" stroke="var(--box-blue)" stroke-width="1.3"><circle cx="7" cy="7" r="6"/><ellipse cx="7" cy="7" rx="2.6" ry="6"/><path d="M1 7h12"/></svg>www.evergreenmindhealth.com</div>
    </div>
  </address>

  <footer class="partners" aria-label="Partner and accreditation badges">
    <span class="badge" style="width:118px;background:#c7c7cf;"></span>
    <span class="badge" style="width:150px;background:#c9cede;"></span>
    <span class="badge" style="width:90px;background:#dccbd6;"></span>
    <span class="badge" style="width:150px;background:#c6d3e6;"></span>
    <span class="badge" style="width:190px;background:#c6d3e6;"></span>
  </footer>
</main>
</body>
</html>
```